Tarrow Building Performance

Id like for my business card to be very bold and professional. Incorporating the business logo, the main services offered, and my contact info. Services are spray foam, insulation, new construction, retrofit, weatherization.

When opening this project sketch harbor was not able to upload my new logo that I picked from another recent sketch harbor project. Does anyone know how i could upload my logo onto the page for design of the business cards?

Target Market(s)

Building owners, contractors

Industry/Entity Type

Building Insulation and performance improvements

Contact Information for Business Card

Owner, Email dean@tarrowbuildingperformance.example Phone number 555-208-6147

Colors
0054AA
0677BA
7BADD7
CADEEF
E8F1F8
F0912C
F2A743
F7CA91
FBE8D2
FDF5EE

Requirements
Must have
• Services- spray foam, cellulose, mineral wool, fiberglass, air sealing, new construction, retrofit, weatherization, energy saving assesments

```html
<!DOCTYPE html>
<html lang="en">
<head>
<meta charset="utf-8">
<title>Tarrow Building Performance – Business Card</title>
<link href="https://fonts.googleapis.com/css2?family=Roboto:wght@400;500;700;900&display=swap" rel="stylesheet">
<style>
  :root {
    --navy: #131a35;
    --navy-deep: #0f1631;
    --orange: #e8730f;
    --sky: #5ab4e5;
    --white: #ffffff;
    --stage: #bdbdbd;
  }
  * { box-sizing: border-box; margin: 0; padding: 0; }
  html, body { width: 1200px; height: 802px; overflow: hidden; }
  body {
    background: var(--stage);
    font-family: "Roboto", sans-serif;
    display: flex;
    align-items: center;
    justify-content: center;
    gap: 40px;
  }
  .card {
    position: relative;
    width: 520px;
    height: 297px;
    border-radius: 22px;
    background: var(--navy);
    overflow: hidden;
    box-shadow: 0 12px 28px rgba(0,0,0,0.35);
  }
  .card--back { background: var(--navy-deep); }

  /* edge bands on the front */
  .edge-bottom { position: absolute; left: 0; right: 0; bottom: 0; height: 8px; background: var(--sky); }
  .edge-right { position: absolute; top: 0; bottom: 8px; right: 0; width: 8px; background: var(--orange); }

  /* wordmark */
  .brand { position: absolute; display: flex; align-items: center; gap: 12px; }
  .brand__mark { width: 22px; height: 22px; background: var(--sky); flex: none; }
  .brand__name {
    font-weight: 900;
    color: var(--orange);
    text-transform: uppercase;
    line-height: 1.05;
    letter-spacing: 0.5px;
  }
  .brand__rule { position: absolute; height: 5px; background: var(--sky); }

  .card--front .brand { left: 44px; top: 52px; }
  .card--front .brand__name { font-size: 30px; }
  .card--front .brand__rule { left: 44px; top: 132px; width: 360px; }

  .person { position: absolute; left: 44px; top: 180px; text-align: right; width: 160px; }
  .person__name { font-size: 22px; font-weight: 700; color: var(--sky); }
  .person__role { font-size: 15px; color: var(--white); margin-top: 4px; }
  .divider { position: absolute; left: 218px; top: 174px; width: 1px; height: 60px; background: var(--orange); }

  .contact { position: absolute; left: 234px; top: 178px; list-style: none; }
  .contact li { display: flex; align-items: center; gap: 8px; color: var(--white); font-size: 13px; margin-bottom: 14px; }
  .contact svg { width: 16px; height: 16px; flex: none; }

  /* back */
  .card--back .brand { left: 60px; top: 40px; }
  .card--back .brand__name { font-size: 30px; }
  .card--back .brand__rule { left: 60px; top: 120px; width: 400px; }

  .services-head { position: absolute; left: 30px; right: 30px; top: 148px; display: flex; align-items: center; gap: 12px; }
  .services-head::before, .services-head::after { content: ""; flex: 1; height: 1px; background: var(--white); }
  .services-head h2 { font-size: 22px; font-weight: 700; color: var(--sky); letter-spacing: 0.5px; }

  .services { position: absolute; left: 30px; right: 30px; top: 192px; list-style: none; display: flex; flex-wrap: wrap; justify-content: center; gap: 8px 16px; }
  .services li { font-size: 15px; color: var(--white); display: flex; align-items: center; gap: 7px; }
  .services li::before { content: ""; width: 5px; height: 5px; border-radius: 50%; background: var(--orange); }
</style>
</head>
<body>

  <section class="card card--front">
    <div class="brand">
      <span class="brand__mark"></span>
      <span class="brand__name">Tarrow<br>Building Performance</span>
    </div>
    <div class="brand__rule"></div>

    <div class="person">
      <p class="person__name">Marcus Ellery</p>
      <p class="person__role">Owner</p>
    </div>
    <div class="divider"></div>
    <ul class="contact">
      <li>
        <svg viewBox="0 0 24 24" aria-hidden="true"><path fill="#e8730f" d="M6.6 10.8a15.1 15.1 0 0 0 6.6 6.6l2.2-2.2a1 1 0 0 1 1-.25 11.4 11.4 0 0 0 3.6.57 1 1 0 0 1 1 1V20a1 1 0 0 1-1 1A17 17 0 0 1 3 4a1 1 0 0 1 1-1h3.5a1 1 0 0 1 1 1c0 1.25.2 2.45.57 3.57a1 1 0 0 1-.25 1z"/></svg>
        555-208-6147
      </li>
      <li>
        <svg viewBox="0 0 24 24" aria-hidden="true"><path fill="#e8730f" d="M2 5h20v14H2z"/><path fill="none" stroke="#131a35" stroke-width="2" d="M2 5l10 8 10-8"/></svg>
        dean@tarrowbuildingperformance.example
      </li>
    </ul>

    <div class="edge-right"></div>
    <div class="edge-bottom"></div>
  </section>

  <section class="card card--back">
    <div class="brand">
      <span class="brand__mark"></span>
      <span class="brand__name">Tarrow<br>Building Performance</span>
    </div>
    <div class="brand__rule"></div>

    <div class="services-head"><h2>OUR SERVICES</h2></div>
    <ul class="services">
      <li>Spray foam</li>
      <li>Cellulose</li>
      <li>Mineral wool</li>
      <li>Fiberglass</li>
      <li>Air sealing</li>
      <li>New construction</li>
      <li>Retrofit</li>
      <li>Weatherization</li>
      <li>Energy saving</li>
      <li>Assesments</li>
    </ul>
  </section>

</body>
</html>
```